Business Card Design Project

We need a hip business card! We are a bakery that specializes in bite sized treats! We do not like foo-foo things, rather have a hip, edgy nature about our style. Our head baker has lots of tattoos....basically, we are not going for the tea party look. We have uploaded our logo, which has a character in it...because we still want to be fun and friendly to little peeps...

Colors: Red and Black
Use : Existing logo
Info: name, address, telephone #, email, URL

Industry/Entity Type

Bakery

Requirements
Must have
• logo: will upload
font: serfiffic grunge
feel: hip and cool, somewhat edgy yet still fun

```html
<!DOCTYPE html>
<html lang="en">
<head>
<meta charset="utf-8">
<title>Small Sin bake shop – business card</title>
<link rel="stylesheet" href="https://fonts.googleapis.com/css2?family=Alegreya:wght@700&display=swap">
<style>
  :root {
    --backdrop: #f3f2ef;
    --kraft: #c8a676;
    --kraft-edge: #b08d5e;
    --ink: #1e1a17;
    --devil-red: #d8343c;
    --handwriting-tone: #8e7350;
  }
  * { margin: 0; padding: 0; box-sizing: border-box; }
  html, body {
    width: 1200px;
    height: 900px;
    overflow: hidden;
    background: var(--backdrop);
  }
  .canvas {
    position: relative;
    width: 1200px;
    height: 900px;
  }
  .card {
    position: absolute;
    left: 110px;
    top: 170px;
    width: 980px;
    height: 560px;
  }
  .card-shape {
    position: absolute;
    inset: 0;
    width: 980px;
    height: 560px;
  }
  .brand {
    position: absolute;
    left: 200px;
    top: 105px;
    display: flex;
    align-items: center;
    gap: 28px;
  }
  .brand-mark {
    width: 110px;
    height: 110px;
    border-radius: 50%;
    background: var(--devil-red);
    flex: none;
  }
  .brand-name {
    font-family: "Alegreya", Georgia, serif;
    font-weight: 700;
    color: var(--ink);
    line-height: 1;
  }
  .brand-name .word {
    display: block;
    font-size: 96px;
    letter-spacing: 2px;
  }
  .brand-name .tagline {
    display: block;
    font-size: 40px;
    margin-top: 6px;
    text-align: right;
  }
  .handwritten-contact {
    position: absolute;
    left: 150px;
    top: 330px;
    width: 580px;
    height: 78px;
    border-radius: 6px;
    background: var(--handwriting-tone);
  }
</style>
</head>
<body>
  <main class="canvas">
    <section class="card">
      <svg class="card-shape" viewBox="0 0 980 560" aria-hidden="true">
        <path d="M0,0 H980 V200 A80,80 0 0 0 980,360 V560 H0 Z"
              fill="var(--kraft)" stroke="var(--kraft-edge)" stroke-width="2"/>
      </svg>
      <div class="brand">
        <span class="brand-mark" aria-hidden="true"></span>
        <h1 class="brand-name">
          <span class="word">SMALL SIN</span>
          <span class="tagline">bake shop</span>
        </h1>
      </div>
      <div class="handwritten-contact" role="img"
           aria-label="Hand-written staff name and phone number in black marker"></div>
    </section>
  </main>
</body>
</html>
```